Business Card Design for Event Planning Company

Create a business card for event planning company using our new logo. After I pick the design, I will need files made for 6 employees. Our company provides event design & logistics services as well as venue management. The font should be sans serif and complementary to the logo. I will need to know the name of the font selected for the final design. The phone numbers listed should be separated by "." not "-"

Address for the card
PO Box 318, Washington, DC 20019

Card One
Lorna Pettibone
lpettibone@galavoyant.com
202.481.7730

Card Two
Miriam Okonkwo
mokonkwo@galavoyant.com
202.556.2047

Card Three
Tessa Varnholt
tvarnholt@galavoyant.com
978.620.4471

Card Four
Robin Fess
rfess@galavoyant.com
202.718.3362

Card Five
Ada-Rose Pelletan-Uzor
adarose@galavoyant.com
202.839.1205

Card Six
Beatrix Holloway
Beatrix@galavoyant.com
202.492.6618

Target Market(s)

Corporate/Non-Profit

Industry/Entity Type

Event Planning

Contact Information for Business Card

Address for the card

Card One
Lorna Pettibone
lpettibone@galavoyant.com
202.481.7730

Card Two
Miriam Okonkwo
202.556.2047

Card Three
Tessa Varnholt
978.620.4471

Card Four
Robin Fess
rfess@galavoyant.com
202.718.3362

Card Five
Ada-Rose Pelletan-Uzor
202.839.1205

Card Six
Beatrix Holloway
202.492.6618

Font styles to use
Sans Serif

Colors

Designer to choose colors to be used in the design.

Requirements
Must have
• Two-sided with logo
Should not have
• Extra colors or be too busy

```html
<!DOCTYPE html>
<html lang="en">
<head>
<meta charset="utf-8">
<title>Galavoyant Business Card</title>
<link rel="stylesheet" href="https://fonts.googleapis.com/css2?family=Questrial&display=swap">
<style>
  :root {
    --backdrop: #2a2a2b;
    --card-white: #ffffff;
    --card-grey: #e9e9ea;
    --ink: #1e1e1f;
    --charcoal: #272627;
    --teal: #4e8f8b;
    --teal-light: #6fb0ab;
    --soft-text: #e6e6e6;
  }
  * { box-sizing: border-box; margin: 0; padding: 0; }
  html, body { width: 1200px; height: 997px; overflow: hidden; }
  body {
    background: var(--backdrop);
    font-family: "Questrial", "Century Gothic", sans-serif;
    position: relative;
  }
  .card {
    position: absolute;
    left: 290px;
    width: 620px;
    height: 354px;
    border-radius: 22px;
    overflow: hidden;
  }
  .card-back {
    top: 100px;
    background: linear-gradient(135deg, var(--card-white) 0%, var(--card-grey) 100%);
  }
  .card-front { top: 520px; background: var(--card-white); }
  .card-art { position: absolute; inset: 0; width: 100%; height: 100%; }

  .wordmark {
    display: flex;
    align-items: center;
    gap: 12px;
    color: var(--ink);
    font-weight: 400;
    letter-spacing: 1px;
  }
  .wordmark-dot {
    width: 22px; height: 22px;
    border-radius: 50%;
    background: var(--teal);
    flex: none;
  }
  .card-back .wordmark {
    position: absolute; right: 36px; bottom: 40px;
    font-size: 36px;
  }
  .card-front .wordmark {
    position: absolute; top: 52px; left: 0; right: 0;
    justify-content: center;
    font-size: 56px;
  }
  .card-front .wordmark-dot { width: 30px; height: 30px; }

  .holder {
    position: absolute; top: 162px; left: 0; right: 0;
    text-align: center;
  }
  .holder-name { color: var(--card-white); font-size: 21px; letter-spacing: 0.5px; }
  .holder-title { color: var(--ink); font-size: 14px; margin-top: 4px; }

  .website {
    position: absolute; right: 30px; top: 240px;
    color: var(--teal-light); font-size: 15px; letter-spacing: 0.5px;
  }
  .contacts {
    position: absolute; left: 30px; bottom: 26px;
    list-style: none;
  }
  .contacts li {
    display: flex; align-items: center; gap: 12px;
    color: var(--soft-text); font-size: 17px;
    margin-top: 7px;
  }
  .contact-icon {
    width: 20px; height: 20px; border-radius: 50%;
    background: var(--teal);
    display: flex; align-items: center; justify-content: center;
    flex: none;
  }
  .contact-icon svg { width: 12px; height: 12px; fill: var(--charcoal); }
</style>
</head>
<body>

<section class="card card-back" aria-label="Card back">
  <div class="wordmark"><span class="wordmark-dot"></span><span>galavoyant</span></div>
</section>

<section class="card card-front" aria-label="Card front">
  <svg class="card-art" viewBox="0 0 620 354" preserveAspectRatio="none" aria-hidden="true">
    <rect x="0" y="200" width="620" height="154" fill="var(--charcoal)"/>
    <rect x="0" y="192" width="620" height="8" fill="var(--teal)"/>
    <polygon points="150,200 180,152 440,152 470,200 445,226 175,226" fill="var(--teal)"/>
  </svg>

  <div class="wordmark"><span class="wordmark-dot"></span><span>galavoyant</span></div>

  <div class="holder">
    <p class="holder-name">Lorna Pettibone</p>
    <p class="holder-title">Director</p>
  </div>

  <p class="website">www.galavoyant.com</p>

  <ul class="contacts">
    <li>
      <span class="contact-icon"><svg viewBox="0 0 24 24"><path d="M6.6 10.8a15 15 0 0 0 6.6 6.6l2.2-2.2a1 1 0 0 1 1-.25 11.4 11.4 0 0 0 3.6.57 1 1 0 0 1 1 1V20a1 1 0 0 1-1 1A17 17 0 0 1 3 4a1 1 0 0 1 1-1h3.5a1 1 0 0 1 1 1c0 1.25.2 2.45.57 3.6a1 1 0 0 1-.25 1z"/></svg></span>
      202.481.7730
    </li>
    <li>
      <span class="contact-icon"><svg viewBox="0 0 24 24"><path d="M2 5h20v14H2z M4 7v.5l8 5 8-5V7l-8 5z" fill-rule="evenodd"/></svg></span>
      lpettibone@galavoyant.com
    </li>
    <li>
      <span class="contact-icon"><svg viewBox="0 0 24 24"><path d="M12 2a7 7 0 0 0-7 7c0 5 7 13 7 13s7-8 7-13a7 7 0 0 0-7-7zm0 9.5A2.5 2.5 0 1 1 12 6.5a2.5 2.5 0 0 1 0 5z"/></svg></span>
      PO Box 318, Washington, DC 20019
    </li>
  </ul>
</section>

</body>
</html>
```